Coaching Business Needs a Website

Business Name: Bright Orbit Coaching
My Name: Martin Hollowbrook

I am a human behaviour expert that needs not just a website, but in the process a "personality" for my brand (Bright Orbit).

With your brilliance and creativity, I want my reputation to be the go to expert in changing unresourceful human behaviour (eg. smoking, eating sugar, procrastination, overwhelm, fear, laziness, weight-gain, phobias, lack of motivation, etc).

===========================
Page 1 (Titled: 'Start Here')

My tag line is "Bright Orbit". The home page should be friendly, inviting, exciting, empowering, positive and innovative.

My Mission Quote: (so people know why I do what I do)

"Our mission is to improve as many people's lives as we can, when we can, through workshops, being guest speaker at events, coaching/mentoring and with valuable products." - Martin Hollowbrook, Human Behaviour Expert (I will give you a photo of me to put with this quote).

My marketing strategy is to share how I ride, because that is my focus (the experience that clients get). Please show the following on my Page 1:

- My mission quote (see above).
- A video (please insert any video at this stage, as I will get a marketing video professionally made to go on this page 1 of my website).
- 10 Reasons Why People Choose 'Bright Orbit Coaching'.
- What We Offer (with Call To Action Buttons, see below).
- Success Stories (these are our Testimonials).

-------------------------------------------
10 Reasons Why People Choose 'Bright Orbit Coaching':

Reason No. 1 We know how to make Bright Orbit in other people's lives. This is our favourite method of making change.

Reason No. 2 We give away a lot of FREE stuff.

Reason No. 3 We thank you for accepting FREE stuff. We are genuinely grateful for you accepting our FREE stuff.

Reason No. 4 We give you a feeling of belonging.

Reason No. 5 We give you the feeling that you are special, because you are.

Reason No. 6 We give you the feeling of significance, because you deserve it.

Reason No. 7 We give you the feeling of feeling good.

Reason No. 8 We give you positive, empowering experiences.

Reason No. 9 We give you tools, models and methodologies to improve every area of your life, continuously for the rest of your life. You can have fulfillment.

Reason No. 10 We give you value beyond what you can imagine.

What We Offer: (each of the following with a picture and more details)

1. Personal Coaching / Mentoring (more details: 1st Session FREE, valued at A$125, Unlimited chat support, call to action button to go to https://bookwell.example/brightorbitcoaching).

2. Human Behaviour Events (more details: next upcoming event, call to action button to go to... I will provide later.. I want to be able to change this hyperlink regularly to the latest upcoming event).

3. Guest Speaker / Master of Ceremonies (call to action button to go to 'Contact Us' website page).

4. Great Value Products (call to action button to go to 'Products' website page).

5. Great FREE Information (call to action button to go to 'Blogs' website page).

Success Stories:

Please allow for 10 written testimonial stories to be added. Please put 10 random text ones so I know what it will look like. I want to be able to change the text in the future. It would be good to put the person's picture and a star rating (eg. 5 stars).

Page 2 (Title: 'Products')

A place where I can add products...

Page 3 (Titled: 'Blogs')

A place where I can add written blogs...

Page 4 (Titled: 'Contact Us')

Contact us form with:
- Name
- Email Address
- Contact Number
- Message

Thank you. I look forward to working with you!!! I will upload my Logo for you to use.

Target Market(s)

Real, Everyday People - Men & Women aged between 21 - 50, who want to change several behaviours in their health, career, relationship, etc, that they feel are holding them back.

Industry/Entity Type

Life Coaching

Contact Information for Business Card

My Name: Martin Hollowbrook, Bright Orbit Expert
Mobile: xxxxxxxxxxxxxx
Email: xxxxxxxxxxxxxx@mailbox.example
Website: brightorbitcoaching.example.au

On the back have what we do:
1. Personal Coaching / Mentoring
2. Human Behaviour Events
3. Guest Speaker / Master of Ceremonies

Coding

Coded - Design and coding required

Number of Pages Required

4 page

Colors
ffc214

Requirements
Must have
• Inspiring images... My website must come across as fun, social, happy, and inviting. The website must have a personality; it is a marketing lead generation tool. It must represent Martin Hollowbrook as being a Human Behaviour Expert (ie. video & testimonials) and must have Call To Action buttons. The website should look professional, not something done using a cheap template. The colour selected is GOLD.
Nice to have
• Additional creative functionality...
Should not have
• It should not have anything negative on it.

```html
<!DOCTYPE html>
<html lang="en">
<head>
<meta charset="utf-8">
<title>Bright Orbit Coaching – Start Here</title>
<link href="https://fonts.googleapis.com/css2?family=Fira+Sans+Condensed:wght@400;500;600;700&family=Hind:wght@400;500&family=Kaushan+Script&display=swap" rel="stylesheet">
<style>
:root{
  --gold:#ffc214;
  --gold-deep:#f5b400;
  --gold-soft:#ffd04a;
  --ink:#1f1f1f;
  --text:#3a3a3a;
  --muted:#6b6b6b;
  --white:#ffffff;
  --grey-band:#ececec;
  --footer:#231f20;
  --star:#f4b400;
}
*{box-sizing:border-box;margin:0;padding:0}
html,body{width:1200px;height:3156px;overflow:hidden}
body{position:relative;background:var(--white);font-family:"Hind",Arial,sans-serif;color:var(--text)}
.abs{position:absolute}
.head{font-family:"Fira Sans Condensed",Arial,sans-serif;font-weight:700;text-transform:uppercase;color:var(--ink)}
.script{font-family:"Kaushan Script",cursive;color:var(--ink)}

/* hero */
.hero{left:0;top:0;width:1200px;height:562px;overflow:hidden;
  background:radial-gradient(circle at 50% 55%,#f7e2c6 0%,#e9b98f 28%,#d98d5a 48%,#c9632e 66%,#f2c233 100%)}
.hero-shade{left:0;top:0;width:1200px;height:120px;background:linear-gradient(#f6b21acc,#f6b21a00)}
.hero-title{left:0;top:24px;width:1200px;text-align:center;font-size:17px;color:var(--white)}
.hero-sub{left:0;top:46px;width:1200px;text-align:center;font-size:16px;color:var(--white);letter-spacing:.3px;text-transform:uppercase}
.hero-mark{left:520px;top:200px;width:160px;height:160px;border-radius:50%;background:var(--white);
  display:flex;align-items:center;justify-content:center;text-align:center;font-family:"Fira Sans Condensed",Arial,sans-serif;font-weight:700;font-size:24px;line-height:1.05;color:var(--ink)}

/* nav */
.nav{left:0;top:562px;width:1200px;height:44px;background:var(--white)}
.nav-brand{left:248px;top:8px;display:flex;align-items:center;gap:8px;font-family:"Fira Sans Condensed",Arial,sans-serif;font-weight:700;font-size:15px;color:var(--ink);text-transform:uppercase}
.nav-brand i{display:block;width:26px;height:26px;border-radius:50%;background:var(--gold)}
.nav-links{left:427px;top:14px;display:flex;font-size:13px;color:var(--ink);text-transform:uppercase}
.nav-links span{padding:0 22px;border-left:1px solid #555;line-height:13px}
.nav-links span:first-child{border-left:0;padding-left:0}
.nav-social{left:808px;top:10px;display:flex;gap:6px}
.nav-social i{display:block;width:24px;height:24px;border-radius:50%;background:#4a4a4a}

/* welcome */
.welcome{left:0;top:606px;width:1200px;height:329px;background:var(--gold)}
.welcome-kicker{left:0;top:40px;width:1200px;text-align:center;font-size:19px}
.welcome-name{left:0;top:64px;width:1200px;text-align:center;font-size:31px}
.welcome-photo{left:558px;top:125px}
.welcome-person{left:0;top:226px;width:1200px;text-align:center;font-size:19px}
.welcome-mission{left:360px;top:253px;width:480px;text-align:center;font-size:12.5px;line-height:20px;color:var(--ink)}

/* video */
.video{left:0;top:935px;width:1200px;height:328px;background:linear-gradient(135deg,#f4f4f4,#e4e4e4 50%,#f4f4f4)}
.video-title{left:248px;top:70px;font-size:19px}
.video-copy{left:248px;top:104px;width:245px;font-size:12px;line-height:18px;color:var(--text)}
.video-copy p+p{margin-top:18px}
.video-frame{left:522px;top:44px;width:429px;height:242px;box-shadow:0 8px 16px rgba(0,0,0,.25);overflow:hidden}
.video-still{width:100%;height:100%;background:linear-gradient(#f3a13a 0%,#f7c25a 45%,#f29a2a 62%,#c9651d 100%)}
.video-play{left:186px;top:92px}
.video-bar{left:0;top:222px;width:429px;height:20px;background:rgba(0,0,0,.55)}

/* reasons */
.reasons{left:0;top:1263px;width:1200px;height:741px;background:var(--gold)}
.reasons-kicker{left:248px;top:56px;font-family:"Fira Sans Condensed",Arial,sans-serif;font-size:20px;color:#6b4d00;text-transform:uppercase}
.reasons-name{left:248px;top:80px;font-size:22px}
.reasons-label{left:550px;top:40px;font-size:20px}
.timeline{left:600px;top:80px;width:4px;height:573px;background:var(--ink)}
.dot{width:12px;height:12px;border-radius:50%;background:var(--ink)}
.reason{width:330px}
.reason b{display:block;font-family:"Fira Sans Condensed",Arial,sans-serif;font-size:27px;font-weight:700;color:var(--ink);line-height:28px}
.reason p{font-size:11.5px;line-height:17px;color:var(--ink)}
.reason.right{left:621px}
.reason.left{left:251px;text-align:right}

/* offer */
.offer-title{left:0;top:2040px;width:1200px;text-align:center;font-size:17px}
.offer{width:230px;text-align:center}
.offer svg{display:block;margin:0 auto}
.offer h3{margin-top:14px;font-size:15px;line-height:18px}
.offer p{margin-top:6px;font-size:11.5px;line-height:16px;color:var(--text);height:34px}
.btn{display:inline-block;margin-top:6px;width:126px;height:27px;line-height:28px;background:var(--gold);font-family:"Fira Sans Condensed",Arial,sans-serif;font-weight:600;font-size:11px;letter-spacing:1.5px;color:var(--ink);text-transform:uppercase}

/* stories */
.stories{left:0;top:2537px;width:1200px;height:294px;background:linear-gradient(90deg,#dcdcdc,#eeeeee 40%,#e2e2e2)}
.stories-title{left:0;top:36px;width:1200px;text-align:center;font-size:17px}
.story{width:320px}
.story-face{width:57px;height:57px;border-radius:50%;border:3px solid var(--white)}
.story-name{left:74px;top:4px;font-family:"Fira Sans Condensed",Arial,sans-serif;font-weight:600;font-size:12px;color:var(--ink);text-transform:uppercase}
.story-text{left:74px;top:70px;width:250px;font-size:11px;line-height:16px;font-style:italic;color:var(--text)}
.stars{left:74px;top:132px;color:var(--star);font-size:13px;letter-spacing:1px}
.dots{left:578px;top:248px;display:flex;gap:6px}
.dots i{display:block;width:5px;height:5px;border-radius:50%;background:#555}
.dots i:first-child{background:var(--ink);width:6px;height:6px}

/* follow */
.follow{left:0;top:2831px;width:1200px;height:169px;background:var(--gold)}
.badge{top:42px;width:225px;height:70px}
.badge-card{left:50px;top:13px;width:175px;height:46px;background:var(--white);border-radius:3px;padding:6px 0 0 24px}
.badge-card strong{display:block;font-family:"Fira Sans Condensed",Arial,sans-serif;font-weight:500;font-size:17px;color:var(--ink);line-height:20px}
.badge-card span{display:block;font-size:8.5px;font-style:italic;color:var(--muted)}
.badge-dot{left:0;top:0;width:70px;height:70px;border-radius:50%;background:var(--ink)}

/* footer */
.footer{left:0;top:3000px;width:1200px;height:156px;background:var(--footer)}
.footer-brand{left:0;top:44px;width:1200px;display:flex;justify-content:center;align-items:center;gap:10px;font-family:"Fira Sans Condensed",Arial,sans-serif;font-weight:700;font-size:22px;color:var(--gold);text-transform:uppercase}
.footer-brand i{display:block;width:36px;height:36px;border-radius:50%;background:var(--gold)}
.footer-copy{left:0;top:110px;width:1200px;text-align:center;font-size:11px;color:#cfcfcf}
</style>
</head>
<body>

<section class="hero abs">
  <div class="abs" style="left:0;top:0;width:1200px;height:562px" role="img" aria-label="Photo of a circle of smiling young people looking down into the camera"></div>
  <div class="hero-shade abs"></div>
  <h1 class="hero-title head abs" style="color:var(--white)">Bright Orbit is fun happy and inviting</h1>
  <p class="hero-sub abs">Lorem Ipsum is simply dummy text of the printing and typesetting industry.</p>
  <div class="hero-mark abs">BRIGHT<br>ORBIT</div>
</section>

<nav class="nav abs">
  <div class="nav-brand abs"><i></i>Bright Orbit</div>
  <div class="nav-links abs"><span>Home</span><span>Products</span><span>Blogs</span><span>Contact Us</span></div>
  <div class="nav-social abs"><i></i><i></i><i></i><i></i><i></i></div>
</nav>

<section class="welcome abs">
  <h2 class="welcome-kicker head abs">Welcome to</h2>
  <p class="welcome-name script abs">Bright Orbit Coaching</p>
  <svg class="welcome-photo abs" width="84" height="94" viewBox="0 0 84 94" role="img" aria-label="Portrait photo of Martin Hollowbrook">
    <polygon points="42,2 82,24 82,70 42,92 2,70 2,24" fill="#6f7a80" stroke="#ffffff" stroke-width="3"/>
  </svg>
  <h3 class="welcome-person head abs">Martin Hollowbrook</h3>
  <p class="welcome-mission abs">My mission is to improve as many people's lives as I can, when I can, through workshops, being guest speaker at events, coaching/mentoring and with valuable products.</p>
</section>

<section class="video abs">
  <h2 class="video-title head abs">A video Bright Orbit Coaching</h2>
  <div class="video-copy abs">
    <p>Lorem Ipsum has been the industry's standard dummy text ever since the 1500s, when an unknown printer took a galley of type and scrambled it to make a type specimen book. It has survived not only five centuries, but also the leap into electronic typesetting, remaining essentially unchanged.</p>
    <p>Lorem Ipsum is simply dummy text of the printing and typesetting industry.</p>
  </div>
  <div class="video-frame abs">
    <div class="video-still" role="img" aria-label="Video still of a golden sunset over the sea"></div>
    <svg class="video-play abs" width="58" height="58" viewBox="0 0 58 58"><circle cx="29" cy="29" r="28" fill="#1f1f1f" opacity=".8"/><polygon points="23,18 41,29 23,40" fill="#ffffff"/></svg>
    <div class="video-bar abs">
      <svg width="429" height="20" viewBox="0 0 429 20"><polygon points="10,6 16,10 10,14" fill="#fff"/><rect x="28" y="9" width="290" height="2" fill="#888"/><rect x="28" y="9" width="40" height="2" fill="#ffffff"/><rect x="380" y="6" width="10" height="8" fill="none" stroke="#fff"/><rect x="400" y="6" width="12" height="8" fill="none" stroke="#fff"/></svg>
    </div>
  </div>
</section>

<section class="reasons abs">
  <p class="reasons-kicker abs">Why people choose</p>
  <p class="reasons-name script abs">“Bright Orbit Coaching”</p>
  <h2 class="reasons-label head abs">Reason no.</h2>
  <div class="timeline abs"></div>
  <div class="dot abs" style="left:596px;top:92px"></div>
  <div class="dot abs" style="left:596px;top:157px"></div>
  <div class="dot abs" style="left:596px;top:229px"></div>
  <div class="dot abs" style="left:596px;top:296px"></div>
  <div class="dot abs" style="left:596px;top:345px"></div>
  <div class="dot abs" style="left:596px;top:402px"></div>
  <div class="dot abs" style="left:596px;top:450px"></div>
  <div class="dot abs" style="left:596px;top:503px"></div>
  <div class="dot abs" style="left:596px;top:551px"></div>
  <div class="dot abs" style="left:596px;top:633px"></div>

  <div class="reason right abs" style="top:73px"><b>01</b><p>We know how to make Bright Orbit in other people's lives. This is our favourite method of making change.</p></div>
  <div class="reason left abs" style="top:138px"><b>02</b><p>We know how to make Bright Orbit in other people's lives. This is our favourite method of making change.</p></div>
  <div class="reason right abs" style="top:210px"><b>03</b><p>We thank you for accepting FREE stuff. We are genuinely grateful for you accepting our FREE stuff.</p></div>
  <div class="reason left abs" style="top:277px"><b>04</b><p>We give you a feeling of belonging.</p></div>
  <div class="reason right abs" style="top:326px"><b>05</b><p>We give you the feeling that you are special, because you are.</p></div>
  <div class="reason left abs" style="top:383px"><b>06</b><p>We give you the feeling of significance, because you deserve it.</p></div>
  <div class="reason right abs" style="top:431px"><b>07</b><p>We give you the feeling of feeling good.</p></div>
  <div class="reason left abs" style="top:484px"><b>08</b><p>We give you positive, empowering experiences.</p></div>
  <div class="reason right abs" style="top:532px"><b>09</b><p>We give you tools, models and methodologies to improve every area of your life, continuously for the rest of your life. You can have fulfillment.</p></div>
  <div class="reason left abs" style="top:614px"><b>10</b><p>We give you value beyond what you can imagine.</p></div>
</section>

<h2 class="offer-title head abs">What we offer</h2>

<div class="offer abs" style="left:24px;top:2088px">
  <svg width="222" height="232" viewBox="0 0 222 232" role="img" aria-label="Photo of a young man beneath a mentor headline">
    <polygon points="118,4 214,58 210,170 104,226 8,172 12,60" fill="none" stroke="#ffc214" stroke-width="1.5"/>
    <polygon points="111,10 205,64 205,172 111,226 17,172 17,64" fill="#3b3b3b"/>
  </svg>
  <h3 class="head">Personal Coaching /<br>Mentoring</h3>
  <p>1st Session FREE, valued at A$125,<br>24/7 chat support</p>
  <span class="btn">Read more</span>
</div>
<div class="offer abs" style="left:253px;top:2088px">
  <svg width="222" height="232" viewBox="0 0 222 232" role="img" aria-label="Photo of an audience at a behaviour event">
    <polygon points="118,4 214,58 210,170 104,226 8,172 12,60" fill="none" stroke="#ffc214" stroke-width="1.5"/>
    <polygon points="111,10 205,64 205,172 111,226 17,172 17,64" fill="#b9bfc2"/>
  </svg>
  <h3 class="head">Human Behaviour<br>Events</h3>
  <p>next upcoming event, call to action<br>button to go to...</p>
  <span class="btn">Read more</span>
</div>
<div class="offer abs" style="left:485px;top:2088px">
  <svg width="222" height="232" viewBox="0 0 222 232" role="img" aria-label="Photo of a speaker holding a microphone">
    <polygon points="118,4 214,58 210,170 104,226 8,172 12,60" fill="none" stroke="#ffc214" stroke-width="1.5"/>
    <polygon points="111,10 205,64 205,172 111,226 17,172 17,64" fill="#8c8c8c"/>
  </svg>
  <h3 class="head">Guest Speaker / Master<br>of Ceremonies</h3>
  <p></p>
  <span class="btn">Contact us</span>
</div>
<div class="offer abs" style="left:714px;top:2088px">
  <svg width="222" height="232" viewBox="0 0 222 232" role="img" aria-label="Photo of a chalkboard with a balance sketch">
    <polygon points="118,4 214,58 210,170 104,226 8,172 12,60" fill="none" stroke="#ffc214" stroke-width="1.5"/>
    <polygon points="111,10 205,64 205,172 111,226 17,172 17,64" fill="#2e2e2e"/>
  </svg>
  <h3 class="head">Great Value<br>Products</h3>
  <p></p>
  <span class="btn">Products</span>
</div>
<div class="offer abs" style="left:946px;top:2088px">
  <svg width="222" height="232" viewBox="0 0 222 232" role="img" aria-label="Photo of a mountain village with a church">
    <polygon points="118,4 214,58 210,170 104,226 8,172 12,60" fill="none" stroke="#ffc214" stroke-width="1.5"/>
    <polygon points="111,10 205,64 205,172 111,226 17,172 17,64" fill="#7d9a8a"/>
  </svg>
  <h3 class="head">Great Free<br>Information</h3>
  <p></p>
  <span class="btn">Blogs</span>
</div>

<section class="stories abs">
  <h2 class="stories-title head abs">Success stories</h2>
  <svg class="abs" style="left:247px;top:164px" width="14" height="20" viewBox="0 0 14 20"><polyline points="11,2 3,10 11,18" fill="none" stroke="#1f1f1f" stroke-width="3"/></svg>
  <svg class="abs" style="left:938px;top:164px" width="14" height="20" viewBox="0 0 14 20"><polyline points="3,2 11,10 3,18" fill="none" stroke="#1f1f1f" stroke-width="3"/></svg>

  <div class="story abs" style="left:288px;top:80px">
    <div class="story-face abs" style="left:0;top:0;background:#8a8f94" role="img" aria-label="Portrait photo of Chris"></div>
    <p class="story-name abs">Chris</p>
    <p class="story-text abs">Lorem Ipsum has been the industry's standard dummy text ever since the 1500s, when an unknown printer took a galley of type and scrambled it to make a type specimen book.</p>
    <p class="stars abs">★★★★★</p>
  </div>
  <div class="story abs" style="left:656px;top:80px">
    <div class="story-face abs" style="left:0;top:0;background:#c9b59a" role="img" aria-label="Portrait photo of James"></div>
    <p class="story-name abs">James</p>
    <p class="story-text abs">Lorem Ipsum has been the industry's standard dummy text ever since the 1500s, when an unknown printer took a galley of type and scrambled it to make a type specimen book.</p>
    <p class="stars abs">★★★★★</p>
  </div>
  <div class="dots abs"><i></i><i></i><i></i><i></i></div>
</section>

<section class="follow abs">
  <div class="badge abs" style="left:242px">
    <div class="badge-card abs"><strong>We're on Circlepage</strong><span>Like us to see our daily updates!</span></div>
    <div class="badge-dot abs"></div>
  </div>
  <div class="badge abs" style="left:482px">
    <div class="badge-card abs"><strong>We're on Chirpline</strong><span>Follow us to see our daily updates!</span></div>
    <div class="badge-dot abs"></div>
  </div>
  <div class="badge abs" style="left:718px">
    <div class="badge-card abs"><strong>We're on Plusring</strong><span>Like us to see our daily updates!</span></div>
    <div class="badge-dot abs"></div>
  </div>
</section>

<footer class="footer abs">
  <div class="footer-brand abs"><i></i>Bright Orbit Coaching</div>
  <p class="footer-copy abs">© 2017 Bright Orbit Coaching, Inc. All rights reserved</p>
</footer>

</body>
</html>
```